Health Care Service Company Flyer

Company name: Tall Orchard Studio
Slogan: Find out what you're made of
Website: tallorchardstudio.ca

I need the flyer to contain the company name (will provide logo source file ASAP), the slogan in large font and a "find out more at orchardstudio.ca"

Other important data to include in the flyer is:
Four bullet points with the following information:
*Track performance and fitness results over time
*Develop proprietary exercise and dietary programs based on actionable data
*Track muscle atrophy from injury, as well as muscle gain during rehabilitation
*Reveal imbalances in muscle symmetry and strength, flexibility, and joint mechanics

I also need the following information conveyed somewhere on the flyer:
*Body Fat, Muscle Mass, and Bone Density Measurements
• Over 50 data points generated in each 10 minute scan
*Call XXX-XXX-XXX to book an appointment today

DEXA Body Composition Services.
Get scanned today.

See example of competitor flyers in the images to get an example of the images and information we are trying to convey

Target Market(s)

athletes, fitness enthusiast, crossfit

Industry/Entity Type

Health And Wellness

Colors
33a6d7
acd036

Requirements
Nice to have
• Prefer images be general health and wellness related - in other words, individuals who look healthy, but are not abnormally muscular
Should not have
• Shirtless models, No big muscles,

```html
<!DOCTYPE html>
<html lang="en">
<head>
<meta charset="utf-8">
<title>Tall Orchard Studio – DEXA Body Composition Flyer</title>
<link href="https://fonts.googleapis.com/css2?family=Orbitron:wght@900&family=Oswald:wght@400;500;600&family=Bebas+Neue&display=swap" rel="stylesheet">
<style>
  :root {
    --ink: #000000;
    --white: #ffffff;
    --brand-blue: #33a6d7;
    --brand-green: #acd036;
    --banner-green: #8cc63f;
    --slogan-fill-top: #d7e86a;
    --slogan-fill-bottom: #7ea21e;
    --slogan-stroke: #2a3310;
    --sticker-blue: #1f6fb5;
    --alert-red: #e41f26;
  }
  * { margin: 0; padding: 0; box-sizing: border-box; }
  html, body { width: 848px; height: 1200px; overflow: hidden; background: var(--ink); }
  .flyer {
    position: relative; width: 848px; height: 1200px; overflow: hidden;
    background: var(--ink); font-family: "Oswald", sans-serif; color: var(--white);
  }
  .brand-name {
    position: absolute; top: 6px; left: 0; width: 848px; text-align: center;
    font-family: "Orbitron", sans-serif; font-weight: 900; font-size: 56px;
    color: var(--brand-blue); line-height: 64px; white-space: nowrap; z-index: 3;
  }
  .photo-couple {
    position: absolute; left: 0; top: 56px; width: 560px; height: 1144px;
    background:
      radial-gradient(ellipse 90px 110px at 205px 140px, #c89a7e 0%, rgba(200,154,126,0) 100%),
      radial-gradient(ellipse 80px 100px at 385px 215px, #d7a98d 0%, rgba(215,169,141,0) 100%),
      radial-gradient(ellipse 220px 420px at 200px 470px, #1c1c1c 0%, rgba(28,28,28,0) 100%),
      radial-gradient(ellipse 120px 120px at 210px 690px, #8c8c8c 0%, rgba(140,140,140,0) 100%),
      radial-gradient(ellipse 140px 520px at 420px 700px, #222 0%, rgba(34,34,34,0) 100%);
    z-index: 1;
  }
  .illustration-anatomy {
    position: absolute; left: 448px; top: 576px; width: 400px; height: 624px;
    background:
      radial-gradient(ellipse 150px 80px at 225px 260px, #8a4a36 0%, rgba(138,74,54,0) 100%),
      radial-gradient(ellipse 80px 100px at 230px 80px, #6f6f6f 0%, rgba(111,111,111,0) 100%),
      radial-gradient(ellipse 240px 380px at 240px 360px, #4e4e4e 0%, rgba(78,78,78,0) 100%);
    z-index: 1;
  }
  .artwork { position: absolute; left: 0; top: 0; width: 848px; height: 1200px; z-index: 4; }
  .tagline { font-family: "Oswald", sans-serif; font-weight: 500; font-size: 30px; fill: var(--white); }
  .sticker-text { font-family: "Bebas Neue", sans-serif; font-size: 34px; fill: var(--white); }
  .slogan-line {
    font-family: "Bebas Neue", sans-serif; font-size: 160px;
    fill: url(#slogan-fill); stroke: var(--slogan-stroke); stroke-width: 7px;
    paint-order: stroke fill; stroke-linejoin: round;
  }
  .band { fill: var(--banner-green); }
  .call-text { font-family: "Bebas Neue", sans-serif; font-size: 48px; fill: var(--alert-red); }
  .scan-text { font-family: "Oswald", sans-serif; font-weight: 500; font-style: italic; font-size: 42px; fill: var(--white); }
  .website { font-family: "Oswald", sans-serif; font-weight: 500; font-size: 74px; fill: var(--brand-green); }
  .service-name { font-family: "Oswald", sans-serif; font-weight: 500; font-size: 32px; fill: var(--alert-red); }
  .benefits {
    position: absolute; left: 36px; top: 657px; width: 500px; list-style: none; z-index: 5;
  }
  .benefits li {
    position: relative; padding-left: 46px; font-size: 23px; line-height: 37.6px;
    font-weight: 500; letter-spacing: -0.3px; white-space: nowrap;
  }
  .benefits .tick { position: absolute; left: 0; top: 4px; }
</style>
</head>
<body>
<main class="flyer">
  <h1 class="brand-name">TALL ORCHARD STUDIO</h1>

  <div class="photo-couple" role="img" aria-label="Smiling fit young man and woman in black workout clothes standing together"></div>
  <div class="illustration-anatomy" role="img" aria-label="Grey anatomical illustration of a human torso with the chest muscles highlighted in red"></div>

  <svg class="artwork" width="848" height="1200" viewBox="0 0 848 1200">
    <defs>
      <linearGradient id="slogan-fill" x1="0" y1="0" x2="0" y2="1">
        <stop offset="0" stop-color="var(--slogan-fill-top)"/>
        <stop offset="1" stop-color="var(--slogan-fill-bottom)"/>
      </linearGradient>
    </defs>

    <text class="tagline" x="32" y="108" textLength="786" lengthAdjust="spacing">BODY FAT- MUSCLE MASS- BONE DENSITY MEASUREMENTS</text>

    <g class="sticker">
      <circle cx="692" cy="264" r="106" fill="var(--white)"/>
      <circle cx="692" cy="264" r="100" fill="var(--sticker-blue)"/>
      <text class="sticker-text" x="690" y="238" text-anchor="middle" textLength="145" lengthAdjust="spacingAndGlyphs">OVER 50 DATA POINTS</text>
      <text class="sticker-text" x="690" y="272" text-anchor="middle" textLength="132" lengthAdjust="spacingAndGlyphs">GENERATED IN EACH</text>
      <text class="sticker-text" x="690" y="306" text-anchor="middle" textLength="108" lengthAdjust="spacingAndGlyphs">10 MINUTE SCAN</text>
      <path d="M712 368 Q760 330 792 282 Q790 340 712 368 Z" fill="#e9e9e9"/>
    </g>

    <g transform="translate(44 414) rotate(-7)">
      <rect class="band" x="0" y="0" width="628" height="118"/>
      <text class="slogan-line" x="52" y="112" textLength="525" lengthAdjust="spacingAndGlyphs">FIND OUT WHAT</text>
    </g>
    <g transform="translate(206 540) rotate(-7)">
      <rect class="band" x="0" y="0" width="628" height="120"/>
      <text class="slogan-line" x="30" y="112" textLength="555" lengthAdjust="spacingAndGlyphs">YOU'RE MADE OF</text>
    </g>

    <g transform="translate(300 958) rotate(-7)">
      <rect class="band" x="0" y="0" width="600" height="54"/>
      <text class="call-text" x="10" y="45" textLength="525" lengthAdjust="spacingAndGlyphs">CALL XXX-XXX-XXX TO BOOK AN APPOINTMENT TODAY</text>
    </g>
    <g transform="translate(570 1038) rotate(-12)">
      <text class="scan-text" x="0" y="0" textLength="190" lengthAdjust="spacingAndGlyphs">Get scanned today</text>
    </g>

    <text class="website" x="96" y="1118" textLength="654" lengthAdjust="spacingAndGlyphs">FIND OUT MORE AT ORCHARDSTUDIO.CA</text>
    <text class="service-name" x="288" y="1168" textLength="272" lengthAdjust="spacingAndGlyphs">DEXA Body Composition Services</text>
  </svg>

  <ul class="benefits">
    <li><svg class="tick" width="36" height="30" viewBox="0 0 36 30"><path d="M2 16 L13 27 L34 3 L29 1 L13 19 L7 12 Z" fill="var(--banner-green)"/></svg>Track performance and fitness results over time</li>
    <li><svg class="tick" width="36" height="30" viewBox="0 0 36 30"><path d="M2 16 L13 27 L34 3 L29 1 L13 19 L7 12 Z" fill="var(--banner-green)"/></svg>Develop proprietary exercise and dietary<br>programs based on actionable data</li>
    <li><svg class="tick" width="36" height="30" viewBox="0 0 36 30"><path d="M2 16 L13 27 L34 3 L29 1 L13 19 L7 12 Z" fill="var(--banner-green)"/></svg>Track muscle atrophy from injury, as well as<br>muscle gain during rehabilitation</li>
    <li><svg class="tick" width="36" height="30" viewBox="0 0 36 30"><path d="M2 16 L13 27 L34 3 L29 1 L13 19 L7 12 Z" fill="var(--banner-green)"/></svg>Reveal imbalances in muscle symmetry and<br>strength, flexibility, and joint mechanics.</li>
  </ul>
</main>
</body>
</html>
```